tovrin company need business card, envelope and letterhead design

Check on the attached file wherein you can find our logo and information about the company
Business card will double sided English version and Arabic version

Industry/Entity Type

Business

Requirements
Must have
• include the design also for the letterhead and envelop
Nice to have

```html
<!DOCTYPE html>
<html lang="en">
<head>
<meta charset="utf-8">
<title>Tovrin Stationery Set</title>
<link href="https://fonts.googleapis.com/css2?family=Exo+2:wght@400;600;700&display=swap" rel="stylesheet">
<style>
  :root {
    --brand-blue: #0b74bf;
    --brand-blue-deep: #0a5ea8;
    --brand-grey: #7c7e81;
    --accent-orange: #e8892c;
    --paper: #ffffff;
    --backdrop: #e3e5e5;
    --ink: #4a4d52;
    --ink-soft: #8a8d92;
  }
  * { box-sizing: border-box; margin: 0; padding: 0; }
  html, body {
    width: 1200px; height: 900px; overflow: hidden;
    background: var(--backdrop);
    font-family: "Exo 2", sans-serif;
  }
  .canvas { position: relative; width: 1200px; height: 900px; }
  .sheet {
    position: absolute;
    box-shadow: 0 4px 14px rgba(0,0,0,.14);
    overflow: hidden;
  }
  .logo {
    display: inline-flex; align-items: center; gap: .35em;
    font-weight: 700; letter-spacing: .08em; text-transform: uppercase;
    line-height: 1;
  }
  .logo-mark { display: inline-block; width: .8em; height: .8em; background: currentColor; }

  /* Letterhead */
  .letterhead { left: 40px; top: 40px; width: 340px; height: 480px; background: var(--paper); }
  .letterhead .logo { position: absolute; left: 22px; top: 22px; font-size: 13px; color: var(--brand-blue); }
  .letterhead-contacts {
    position: absolute; left: 178px; top: 18px; list-style: none;
    font-size: 5px; line-height: 1.55; color: var(--ink-soft);
  }
  .letterhead-contacts li::before {
    content: ""; display: inline-block; width: 4px; height: 4px; margin-right: 3px;
    border: .6px solid var(--ink-soft); vertical-align: middle;
  }
  .letter-meta { position: absolute; left: 18px; top: 70px; width: 60px; text-align: right; }
  .letter-meta dt { font-size: 6px; font-weight: 700; color: var(--brand-blue); }
  .letter-meta dd { font-size: 5px; color: var(--ink-soft); margin-bottom: 6px; }
  .letter-body {
    position: absolute; left: 90px; top: 84px; width: 226px;
    font-size: 5px; line-height: 1.55; color: var(--ink);
  }
  .letter-body p { margin-bottom: 6px; }
  .letter-sign { position: absolute; left: 90px; top: 340px; font-size: 5px; color: var(--ink); line-height: 1.5; }
  .signature-area { width: 74px; height: 16px; margin-top: 8px; background: #e6e7e9; border-radius: 2px; }
  .letterhead-footer { position: absolute; left: 0; bottom: 0; width: 340px; height: 22px; }

  /* Folder */
  .folder {
    left: 410px; top: 40px; width: 340px; height: 480px;
    background: linear-gradient(135deg, var(--brand-blue) 0%, var(--brand-blue-deep) 100%);
  }
  .folder .logo { position: absolute; left: 0; right: 0; top: 150px; justify-content: center; font-size: 30px; color: var(--paper); }
  .folder-graphic {
    position: absolute; left: 60px; right: 0; top: 280px; bottom: 0;
    background: linear-gradient(90deg, rgba(255,255,255,.92) 0%, rgba(255,255,255,.6) 55%, var(--brand-grey) 70%, #6d6f72 100%);
  }

  /* Envelope */
  .envelope { left: 40px; top: 550px; width: 660px; height: 320px; background: var(--brand-blue); }
  .envelope .logo { position: absolute; left: 40px; top: 40px; font-size: 26px; color: var(--paper); }
  .envelope-contacts {
    position: absolute; left: 40px; top: 108px; list-style: none;
    color: var(--paper); font-size: 11px; line-height: 1.75;
  }
  .contact-key {
    display: inline-block; width: 12px; height: 12px; margin-right: 6px;
    background: var(--accent-orange); color: var(--paper);
    font-size: 8px; font-weight: 700; text-align: center; line-height: 12px; vertical-align: middle;
  }
  .envelope-address { padding-left: 18px; }
  .envelope-graphic {
    position: absolute; left: 390px; top: 170px; width: 230px; height: 150px;
    background: linear-gradient(90deg, rgba(255,255,255,.92) 0%, rgba(255,255,255,.6) 50%, var(--brand-grey) 62%, #6d6f72 100%);
  }

  /* Business cards */
  .card { width: 380px; height: 220px; }
  .card-front { left: 780px; top: 40px; background: var(--brand-blue); }
  .card-front .logo { position: absolute; inset: 0; justify-content: center; font-size: 30px; color: var(--paper); }
  .card-back { left: 780px; top: 290px; background: var(--paper); }
  .card-holder {
    position: absolute; left: 0; top: 74px; width: 180px; height: 46px;
    background: var(--brand-blue); color: var(--paper); padding: 9px 0 0 16px;
  }
  .card-holder-name { font-size: 10px; font-weight: 700; }
  .card-holder-role { font-size: 8px; opacity: .85; margin-top: 3px; }
  .card-address {
    position: absolute; left: 196px; top: 46px; width: 184px; height: 30px;
    background: var(--brand-blue); color: var(--paper);
    font-size: 7px; line-height: 1.35; padding: 6px 10px;
  }
  .card-contacts {
    position: absolute; left: 200px; top: 88px; list-style: none;
    font-size: 9px; line-height: 1.8; color: var(--ink);
  }
  .card-contacts .contact-key { background: var(--brand-blue); }
</style>
</head>
<body>
<main class="canvas">

  <section class="sheet letterhead" aria-label="Letterhead">
    <span class="logo"><i class="logo-mark"></i>Tovrin</span>
    <ul class="letterhead-contacts">
      <li>+966 512 480 736</li>
      <li>011 4620 318</li>
      <li>011 4620 319</li>
      <li>hello@tovrin.sa</li>
      <li>Al Noor Street - Al Waha - P.O. Box 4412-11593</li>
    </ul>
    <dl class="letter-meta">
      <dt>Subject</dt><dd>Project Proposal</dd>
      <dt>Date</dt><dd>01/02/2016</dd>
    </dl>
    <div class="letter-body">
      <p>Dear Client,</p>
      <p>Thank you for choosing our team for your next project. We have reviewed your request and prepared a clear plan covering scope, schedule and budget for your approval.</p>
      <p>Our engineers will visit the site next week to confirm measurements and materials. Each stage of the work will be reported to you in writing with photos and notes.</p>
      <p>Payments follow the milestones listed in the attached schedule. Should any change be needed, we will agree on it together before any work continues on site.</p>
      <p>All materials are sourced from approved local suppliers and checked on arrival. Safety rules are followed at all times by every member of our crew.</p>
      <p>We look forward to working with you and remain at your service for any questions. Please contact our office at the number above at your convenience.</p>
      <p>Yours Sincerely,</p>
    </div>
    <div class="letter-sign">
      <div>Adam Harlow</div>
      <div>Executive manager</div>
      <div class="signature-area" role="img" aria-label="Handwritten signature"></div>
    </div>
    <svg class="letterhead-footer" viewBox="0 0 340 22" aria-hidden="true">
      <rect x="0" y="8" width="340" height="14" fill="var(--brand-blue)"/>
      <polygon points="270,22 300,8 340,8 340,22" fill="var(--brand-grey)"/>
      <polygon points="290,22 310,12 340,12 340,22" fill="#a9abad"/>
    </svg>
  </section>

  <section class="sheet folder" aria-label="Presentation folder">
    <span class="logo"><i class="logo-mark"></i>Tovrin</span>
    <div class="folder-graphic" role="img" aria-label="Large brand illustration of white columns beside a grey sword and tower"></div>
  </section>

  <section class="sheet envelope" aria-label="Envelope">
    <span class="logo"><i class="logo-mark"></i>Tovrin</span>
    <ul class="envelope-contacts">
      <li><span class="contact-key">M</span>+966 512 480 736</li>
      <li><span class="contact-key">T</span>011 4620 318</li>
      <li><span class="contact-key">F</span>011 4620 319</li>
      <li><span class="contact-key">E</span>hello@tovrin.sa</li>
      <li><span class="contact-key">A</span>Al Noor Street - Al Waha - P.O. Box 4412-11593</li>
      <li class="envelope-address">Kingdom of Saudi Arabia</li>
    </ul>
    <div class="envelope-graphic" role="img" aria-label="Brand illustration of white columns beside a grey sword and tower"></div>
  </section>

  <section class="sheet card card-front" aria-label="Business card front">
    <span class="logo"><i class="logo-mark"></i>Tovrin</span>
  </section>

  <section class="sheet card card-back" aria-label="Business card back">
    <div class="card-holder">
      <div class="card-holder-name">Faisal Bin Omar Al Rashidi</div>
      <div class="card-holder-role">General Manager</div>
    </div>
    <div class="card-address">Al Noor Street - Al Waha<br>P.O. Box 4412-11593</div>
    <ul class="card-contacts">
      <li><span class="contact-key">M</span>+966 512 480 736</li>
      <li><span class="contact-key">T</span>011 4620 318</li>
      <li><span class="contact-key">F</span>011 4620 319</li>
      <li><span class="contact-key">E</span>hello@tovrin.sa</li>
    </ul>
  </section>

</main>
</body>
</html>
```